Keep Harbor Homes. Avoid short sale, foreclosure, repossession, negative credit inquires and all other negative actions associated with your real estate.

Call 844-27-LUMEN or info@keepharborhomes.example

```html
<!DOCTYPE html>
<html lang="en">
<head>
<meta charset="utf-8">
<title>Keep Harbor Homes – Postcard</title>
<link rel="stylesheet" href="https://fonts.googleapis.com/css2?family=Anton&family=Oswald:wght@500&family=Open+Sans:wght@400;600;700&display=swap">
<style>
  :root {
    --orange: #f0841e;
    --orange-deep: #e5761a;
    --charcoal: #3a3a3a;
    --charcoal-dark: #2a2a2a;
    --paper: #ffffff;
    --panel: #f1f1f1;
    --ink: #4a4a4a;
    --line: #8a8a8a;
    --backdrop: #e6e6e6;
  }
  * { margin: 0; padding: 0; box-sizing: border-box; }
  html, body { width: 689px; height: 1200px; overflow: hidden; }
  body { background: var(--backdrop); position: relative; font-family: "Open Sans", Arial, sans-serif; }

  .postcard {
    position: absolute;
    left: 44px;
    width: 552px;
    height: 367px;
    background: var(--paper);
    transform: scale(1.087);
    transform-origin: top left;
    box-shadow: 0 2px 6px rgba(0,0,0,.18);
  }
  .postcard--front { top: 175px; }
  .postcard--back  { top: 626px; }
  .block { position: absolute; }

  .bg-orange {
    background: linear-gradient(180deg, #f59a3a 0%, var(--orange) 45%, var(--orange-deep) 100%);
  }
  .bg-charcoal {
    background: linear-gradient(180deg, #4a4a4a 0%, var(--charcoal) 50%, var(--charcoal-dark) 100%);
  }

  .headline {
    left: 5px; top: 7px; width: 260px; height: 63px;
    display: flex; align-items: center; justify-content: center;
    font-family: "Anton", Impact, sans-serif;
    font-size: 27px; color: #fff; letter-spacing: .2px;
  }
  .call-box {
    left: 271px; top: 7px; width: 276px; height: 63px;
    display: flex; align-items: center; justify-content: center;
    font-family: "Oswald", "Arial Narrow", sans-serif; font-weight: 500;
    font-size: 31px; color: #fff;
  }
  .call-box .phone { color: var(--orange); margin-left: 9px; }

  .photo { display: block; }
  .photo--money-house {
    left: 5px; top: 77px; width: 195px; height: 153px;
    background: linear-gradient(180deg, #d9e6c4 0%, #a9cc6c 45%, #6fa233 100%);
  }
  .photo--agent-couple {
    left: 205px; top: 112px; width: 342px; height: 218px;
    background: linear-gradient(90deg, #8a5a46 0%, #a56a52 40%, #9a6a58 70%, #7b5345 100%);
  }

  .issue-list {
    left: 5px; top: 235px; width: 195px; height: 95px;
    background: var(--panel);
    list-style: none;
    padding: 14px 0 0 10px;
  }
  .issue-list li {
    font-size: 10.4px; font-weight: 700; color: var(--ink);
    line-height: 15.7px; letter-spacing: .1px;
  }
  .issue-list li::before {
    content: "•"; color: var(--orange); margin-right: 5px;
  }

  .footer-note {
    left: 30px; top: 335px; width: 235px; height: 27px;
    padding: 4px 0 0 10px;
    font-size: 7.6px; font-weight: 600; color: #fff; line-height: 10px;
    text-transform: uppercase;
  }
  .footer-note em { font-style: normal; color: var(--orange); }

  .email-bar {
    display: flex; align-items: center; gap: 8px;
    font-size: 13.4px; color: #fff; font-weight: 600;
  }
  .email-bar svg { flex: none; }
  .postcard--front .email-bar { left: 271px; top: 335px; width: 276px; height: 27px; padding-left: 14px; }

  /* back */
  .photo--happy-couple {
    left: 5px; top: 5px; width: 223px; height: 275px;
    background: linear-gradient(180deg, #e9ecee 0%, #cfd4d6 55%, #a7adb0 100%);
  }
  .back-call {
    left: 5px; top: 285px; width: 257px; height: 40px;
    display: flex; align-items: center; justify-content: center;
    font-family: "Oswald", "Arial Narrow", sans-serif; font-weight: 500;
    font-size: 27px; color: #fff;
  }
  .postcard--back .email-bar {
    left: 30px; top: 330px; width: 232px; height: 32px;
    background: var(--panel); color: var(--ink); font-weight: 400; font-size: 11.5px;
    padding-left: 14px;
  }
  .stamp { left: 453px; top: 18px; width: 76px; height: 76px; border: 1px solid var(--line); }
  .address-line { left: 303px; width: 224px; height: 1px; background: var(--line); }
</style>
</head>
<body>

<section class="postcard postcard--front" aria-label="Postcard front">
  <h1 class="block headline bg-orange">AVOID FORECLOSURE</h1>
  <div class="block call-box bg-charcoal">Call<span class="phone">844-27-LUMEN</span></div>

  <div class="block bg-charcoal" style="left:205px; top:77px; width:60px; height:30px;"></div>
  <div class="block bg-orange" style="left:271px; top:77px; width:276px; height:30px;"></div>

  <div class="block photo photo--money-house" role="img" aria-label="Photo: hand placing a folded banknote house on green grass"></div>
  <div class="block photo photo--agent-couple" role="img" aria-label="Photo: agent talking with a smiling senior couple outside a brick house"></div>

  <ul class="block issue-list">
    <li>AVOID SHORT SALE</li>
    <li>FORECLOSURE</li>
    <li>REPOSSESSION</li>
    <li>NEGATIVE CREDIT INQUIRES</li>
  </ul>

  <div class="block bg-orange" style="left:5px; top:335px; width:20px; height:27px;"></div>
  <p class="block footer-note bg-charcoal">And all other <em>negative actions</em> associated<br>with your <em>real estate.</em></p>

  <div class="block email-bar bg-orange">
    <svg width="12" height="9" viewBox="0 0 12 9" aria-hidden="true"><rect x=".5" y=".5" width="11" height="8" fill="none" stroke="#fff"/><path d="M.5 .5 6 5l5.5-4.5" fill="none" stroke="#fff"/></svg>
    <span>info@keepharborhomes.example</span>
  </div>
</section>

<section class="postcard postcard--back" aria-label="Postcard back">
  <div class="block photo photo--happy-couple" role="img" aria-label="Photo: happy couple giving thumbs up in front of a white house"></div>
  <div class="block bg-orange" style="left:233px; top:5px; width:29px; height:227px;"></div>
  <div class="block bg-charcoal" style="left:233px; top:237px; width:29px; height:43px;"></div>

  <div class="block back-call bg-orange">Call 844-27-LUMEN</div>

  <div class="block bg-charcoal" style="left:5px; top:330px; width:20px; height:32px;"></div>
  <div class="block email-bar">
    <svg width="12" height="9" viewBox="0 0 12 9" aria-hidden="true"><rect x=".5" y=".5" width="11" height="8" fill="none" stroke="#f0841e"/><path d="M.5 .5 6 5l5.5-4.5" fill="none" stroke="#f0841e"/></svg>
    <span>info@keepharborhomes.example</span>
  </div>

  <div class="block stamp"></div>
  <div class="block address-line" style="top:195px;"></div>
  <div class="block address-line" style="top:233px;"></div>
  <div class="block address-line" style="top:272px;"></div>
</section>

</body>
</html>
```